Need a Zine cover designed

I’m looking for someone who can design an eye catching and original zine cover. Incorporating the logo I included below. I’m not 100% sure which logo I want to use on the cover, if it’s possible to see how you incorporate the logos on a sample will make it easier for me to decide. Thank you for your time.
For the second logo I’m unsure how to remove the grey background, but I do not want it included in the zine cover
The title of the zine is:
Velvet Orchard
perspectives of culture, life, & love

```html
<!DOCTYPE html>
<html lang="en">
<head>
<meta charset="utf-8">
<title>Velvet Orchard — Zine Cover</title>
<link rel="stylesheet" href="https://fonts.googleapis.com/css2?family=Bungee&family=Homemade+Apple&display=swap">
<style>
  :root {
    --page: #ffffff;
    --cover: #1c1c1c;
    --title-pink: #e91e7a;
    --title-blue: #29a8e0;
    --tagline: #ffffff;
    --club-name: #e9a24c;
  }
  html, body {
    margin: 0;
    padding: 0;
    width: 1200px;
    height: 1200px;
    overflow: hidden;
    background: var(--page);
  }
  .canvas {
    position: relative;
    width: 1200px;
    height: 1200px;
  }
  .zine-cover {
    position: absolute;
    left: 289px;
    top: 120px;
    width: 621px;
    height: 960px;
    overflow: hidden;
    background: var(--cover);
  }
  .zine-cover svg {
    display: block;
    width: 621px;
    height: 960px;
  }
  .club-name {
    font-family: "Bungee", sans-serif;
    fill: var(--club-name);
  }
  .title {
    font-family: "Bungee", sans-serif;
  }
  .title-top { fill: var(--title-pink); }
  .title-bottom { fill: var(--title-blue); }
  .tagline {
    font-family: "Homemade Apple", cursive;
    fill: var(--tagline);
  }
</style>
</head>
<body>
<main class="canvas">
  <section class="zine-cover">
    <svg viewBox="0 0 621 960" xmlns="http://www.w3.org/2000/svg">
      <defs>
        <radialGradient id="line-art-tone" cx="50%" cy="55%" r="70%">
          <stop offset="0%" stop-color="#222222"/>
          <stop offset="100%" stop-color="#1c1c1c"/>
        </radialGradient>
      </defs>

      <rect class="background-line-art" x="0" y="0" width="621" height="960"
            fill="url(#line-art-tone)" role="img"
            aria-label="Faint line drawings: flowing curves, sunglasses, lips, a dancing couple and a guitarist"/>

      <g class="club-mark">
        <text class="club-name" x="305" y="172" text-anchor="middle" font-size="40">MELLOW MILE</text>
        <text class="club-name" x="305" y="226" text-anchor="middle" font-size="40">CLUB</text>
      </g>

      <g class="title-block">
        <text class="title title-top" x="8" y="594" font-size="124"
              textLength="640" lengthAdjust="spacingAndGlyphs"
              transform="rotate(-22 8 594)">VELVET</text>
        <text class="title title-bottom" x="62" y="675" font-size="90"
              textLength="575" lengthAdjust="spacingAndGlyphs"
              transform="rotate(-22 62 675)">ORCHARD</text>
        <text class="tagline" x="178" y="700" font-size="19"
              textLength="400" lengthAdjust="spacingAndGlyphs"
              transform="rotate(-26 178 700)">perspectives of culture, life, &amp; love</text>
      </g>
    </svg>
  </section>
</main>
</body>
</html>
```